Business Card Design

We are a new residential construction company.our team is made up of young highly skilled tradesman of the next generation of carpenters coming through with new skills and ideas.we chose the name meridian as it means strikingly different from the rest as this is what we plan to be and we would like to portray this in our business card.we like Bold lettering as we want to make a statement, also the use of colour would be great as we want to stand out from the usual plain construction cards and logos.
I have attached a logo sketch I did as a rough idea if you can tidy it up or improve on it would be good.
I have also attached the LBP logo please include this on the card small but still legible.
open to any colourschemes ideas.
thanks
(note)please delete the LBP#804317 off from the card details please.
Industry/Entity Type
Construction
Contact Information for Business Card
MERIDIAN CONSTRUCTION LIMITED
Director:Tom Halvick
Mobile :0217364820
Email:Meridian.Construction@quillpost.example
Address:48 Wendle place,Ashgrove park 2091,Auckland
LBP#BP804317

```html
<!DOCTYPE html>
<html lang="en">
<head>
<meta charset="utf-8">
<title>Meridian Construction – Business Card</title>
<link href="https://fonts.googleapis.com/css2?family=Open+Sans:wght@400;700;800&display=swap" rel="stylesheet">
<style>
  :root {
    --page-bg: #e6e6e4;
    --card-bg: #0d0e0f;
    --card-bg-soft: #1a1c1e;
    --band-green: #3c7a35;
    --bar-green: #3f8f3a;
    --bar-green-light: #52bd48;
    --rule-green: #3fa83a;
    --brand-lime: #b3d235;
    --label-yellow: #e6d21a;
    --text-white: #f4f4f4;
    --pattern-yellow: #8d8a55;
    --pattern-blue: #6f7392;
    --badge-grey: #cfd2d6;
  }
  * { margin: 0; padding: 0; box-sizing: border-box; }
  html, body {
    width: 1200px; height: 1200px; overflow: hidden;
    background: var(--page-bg);
  }
  .canvas {
    position: relative; width: 1200px; height: 1200px;
    display: flex; align-items: center; justify-content: center;
  }
  .card {
    position: relative; width: 1050px; height: 600px; overflow: hidden;
    background: radial-gradient(ellipse at 70% 40%, var(--card-bg-soft), var(--card-bg) 70%);
    font-family: "Open Sans", Arial, sans-serif;
    box-shadow: 0 10px 30px rgba(0,0,0,.25);
  }
  .card-art { position: absolute; inset: 0; width: 1050px; height: 600px; }
  .band-title {
    font-family: "Open Sans", Arial, sans-serif;
    font-weight: 800; font-size: 27px; fill: var(--text-white);
    letter-spacing: .5px;
  }
  .brand {
    position: absolute; right: 70px; top: 48px; text-align: right;
    color: var(--brand-lime); font-weight: 800; line-height: 1;
  }
  .brand-name { font-size: 54px; letter-spacing: 3px; }
  .brand-sub { font-size: 34px; letter-spacing: 1px; margin-top: 6px; }
  .name-bar {
    position: absolute; left: 520px; top: 215px; width: 480px; height: 80px;
    background: var(--bar-green); text-align: center; padding-right: 80px;
  }
  .name-bar::after {
    content: ""; position: absolute; right: 0; top: 0; width: 78px; height: 100%;
    background: var(--bar-green-light);
  }
  .person-name {
    color: var(--text-white); font-weight: 800; font-size: 32px;
    line-height: 1; padding-top: 13px; letter-spacing: .5px;
  }
  .person-role {
    color: var(--label-yellow); font-weight: 700; font-size: 16px; letter-spacing: 1px;
  }
  .contact {
    position: absolute; right: 70px; top: 322px; width: 480px;
    color: var(--text-white); font-size: 19px; text-align: right;
    white-space: nowrap;
  }
  .contact-row { padding: 7px 0; }
  .contact-row + .contact-row { border-top: 2px solid var(--rule-green); }
  .contact-row:last-child { border-top: none; padding-top: 0; }
  .contact-label { color: var(--label-yellow); }
  .lbp-badge {
    position: absolute; right: 70px; bottom: 30px; width: 46px; height: 46px;
    border-radius: 6px; background: var(--badge-grey);
  }
</style>
</head>
<body>
<main class="canvas">
  <article class="card">
    <svg class="card-art" viewBox="0 0 1050 600">
      <defs>
        <linearGradient id="pattern-tone" x1="0" y1="0" x2="1" y2="1">
          <stop offset="0" stop-color="var(--pattern-yellow)"/>
          <stop offset=".55" stop-color="#5c5c48"/>
          <stop offset="1" stop-color="var(--pattern-blue)"/>
        </linearGradient>
        <linearGradient id="pattern-tone-low" x1="0" y1="0" x2="1" y2="1">
          <stop offset="0" stop-color="var(--pattern-blue)"/>
          <stop offset="1" stop-color="#2a2c36"/>
        </linearGradient>
      </defs>
      <polygon class="pattern-area" role="img" aria-label="Overlapping translucent square pattern in olive and slate tones"
               points="0,0 330,0 0,330" fill="url(#pattern-tone)" opacity=".85"/>
      <polygon class="pattern-area" role="img" aria-label="Overlapping translucent square pattern in slate tones"
               points="0,450 450,0 520,0 0,600" fill="url(#pattern-tone-low)" opacity=".55"/>
      <polygon class="diagonal-band" points="340,0 440,0 0,440 0,340" fill="var(--band-green)"/>
      <line x1="326" y1="0" x2="0" y2="326" stroke="#ffffff" stroke-width="2"/>
      <line x1="454" y1="0" x2="0" y2="454" stroke="#ffffff" stroke-width="2"/>
      <g transform="translate(195,195) rotate(-45)">
        <text class="band-title" x="0" y="-6" text-anchor="middle">MERIDIAN CONSTRUCTION</text>
        <text class="band-title" x="0" y="28" text-anchor="middle">LIMITED</text>
      </g>
    </svg>

    <header class="brand">
      <div class="brand-name">MERIDIAN</div>
      <div class="brand-sub">CONSTRUCTION</div>
    </header>

    <section class="name-bar">
      <div class="person-name">TOM HALVICK</div>
      <div class="person-role">DIRECTOR</div>
    </section>

    <section class="contact">
      <div class="contact-row"><span class="contact-label">Mobile</span> : 0217364820</div>
      <div class="contact-row"><span class="contact-label">Email</span> : Meridian.Construction@quillpost.example</div>
      <div class="contact-row"><span class="contact-label">Address</span> : 48 Wendle place,Ashgrove park 2091</div>
      <div class="contact-row">Auckland</div>
    </section>

    <div class="lbp-badge" role="img" aria-label="Licensed building practitioner badge"></div>
  </article>
</main>
</body>
</html>
```